KSO Talent Growth one-page marketing flyer

Need a modern and stylized one-page marketing flyer for unit of new statewide human resources unit. The reason I am using pixel forum is because our organizations internal communication design standards are bland, boring, and graphic design skills on internal marketing team are limited. There are a handful of requirements we can't ignore in regards to design "look-and-feel", but I'm confident there is talent among the Pixel Forum community that can design something that is clean, modern, and engaging.

I have attached high resolution images, flyer copy, approved RGB colors, and can detail the non-negotiable requirements we must abide by per organization design standards.

Target Market(s)

HR Managers and Executives

Font styles to use
Other font styles liked:
• Helvetica, Alternative Gothic 2

Requirements
Must have
• Refer to the KSO Single Page Template document. This is the primary requirement we must adhere to now matter how the remiander of the flyer is designed. As shown on that template, the top of the front page MUST feature the Capital Night Monday (file name) image, cropped exactly as it apears o the template. The cropped image on the top of the front page must also include the text and magenta colored stripe as that specific color identifies our particular division. The only font types that can be used for the text in the top banner of other copy is Impact and Alternate Gothic No 3 D - no other font types are allowed. Finally, the Approved RGB Colors ( file name) attachment lists the approved RGB colors that can be used for design/copy purposes (*ex. copy can be a shade of gray vs, black).
• Design must be modern. Open to vector type graphic elements or live icons to represent Consulting, Learning Solutions (translation: training/workshops), Tools/Resources
• Size of one-page marketing flyer is 8 1/2 x 11. Copy and graphic design on front and back.

```html
<!DOCTYPE html>
<html lang="en">
<head>
<meta charset="utf-8">
<title>KSO Talent Growth Flyer</title>
<link href="https://fonts.googleapis.com/css2?family=Oswald:wght@400;500&family=Pathway+Gothic+One&family=Roboto+Condensed:ital,wght@1,300;1,400&display=swap" rel="stylesheet">
<style>
  :root {
    --magenta: #a3007e;
    --charcoal: #434343;
    --ink: #3a3a3a;
    --band-gray: #464646;
    --night: #2c4a8a;
    --white: #ffffff;
  }
  * { margin: 0; padding: 0; box-sizing: border-box; }
  html, body { width: 927px; height: 1200px; overflow: hidden; background: var(--white); }
  .flyer { position: relative; width: 927px; height: 1200px; overflow: hidden; font-family: "Pathway Gothic One", sans-serif; color: var(--ink); }

  .hero { position: absolute; left: 0; top: 0; width: 927px; height: 493px; }
  .hero-photo {
    position: absolute; inset: 0;
    background:
      linear-gradient(90deg, rgba(245,245,245,1) 0%, rgba(240,240,242,0.95) 35%, rgba(240,240,242,0) 60%),
      radial-gradient(ellipse 260px 300px at 470px 260px, #e9e4d6 0%, #c9c2ae 40%, rgba(201,194,174,0) 75%),
      linear-gradient(180deg, #e7eaf2 0%, #6f86c0 35%, var(--night) 60%, #3d4a5a 100%);
  }
  .state-mark { position: absolute; left: 121px; top: 158px; width: 200px; text-align: center;
    font-family: "Oswald", sans-serif; font-weight: 400; color: var(--charcoal); }
  .state-name { font-size: 38px; line-height: 44px; letter-spacing: 0.5px; }
  .state-office { font-size: 15px; line-height: 18px; margin-top: 4px; }

  .unit-badge { position: absolute; left: 169px; top: 285px; width: 98px; height: 98px; border-radius: 50%; background: var(--magenta); }
  .unit-office { position: absolute; left: 60px; top: 388px; font-family: "Oswald", sans-serif; font-size: 25px; color: var(--charcoal); letter-spacing: -0.3px; }
  .unit-name { position: absolute; left: 36px; top: 412px; font-family: "Oswald", sans-serif; font-weight: 500; font-size: 46px; color: var(--magenta); letter-spacing: -0.5px; }

  .services { position: absolute; left: 0; top: 493px; width: 927px; height: 145px; display: flex; }
  .service { display: flex; flex-direction: column; align-items: center; justify-content: flex-end; padding-bottom: 22px; gap: 14px; color: var(--white); background: var(--band-gray); }
  .service--consulting { width: 302px; }
  .service--workshops { width: 319px; background: var(--magenta); }
  .service--tools { width: 306px; }
  .service-label { font-family: "Oswald", sans-serif; font-weight: 500; font-size: 25px; letter-spacing: 0.2px; }
  .service svg { width: 56px; height: 56px; }

  .body-photo { position: absolute; left: 0; top: 638px; width: 927px; height: 562px;
    background: linear-gradient(180deg, #f3f3f3 0%, #ececec 45%, #dcdcdc 75%, #cfcfcf 100%); }

  .column { position: absolute; top: 672px; }
  .column--who { left: 29px; width: 413px; }
  .column--what { left: 483px; width: 414px; }
  .column h2 { font-family: "Oswald", sans-serif; font-weight: 500; font-size: 37px; line-height: 46px; margin-bottom: 6px; letter-spacing: -0.3px; }
  .column--who h2 { color: var(--magenta); }
  .column--what h2 { color: var(--charcoal); }
  .column p { font-size: 18.5px; line-height: 21.7px; text-align: justify; margin-bottom: 9px; }
  .focus-list { list-style: none; margin: 14px 0 10px 12px; }
  .focus-list li { font-size: 18.5px; line-height: 22px; display: flex; align-items: center; gap: 16px; }
  .focus-list li::before { content: ""; width: 12px; height: 12px; background: var(--magenta); }

  .quote { position: absolute; left: 93px; top: 1075px; width: 710px; height: 44px; background: var(--magenta);
    clip-path: polygon(16px 0, 100% 0, 97% 100%, 0 100%); }
  .quote-text { position: absolute; left: 124px; top: 1083px; font-family: "Roboto Condensed", sans-serif; font-style: italic; font-weight: 300; font-size: 17.5px; color: var(--white); }
  .quote-credit { position: absolute; left: 480px; top: 1104px; width: 322px; height: 24px; background: var(--charcoal);
    clip-path: polygon(12px 0, 100% 0, 97% 100%, 0 100%);
    font-family: "Roboto Condensed", sans-serif; font-style: italic; font-size: 13px; color: var(--white); line-height: 24px; padding-left: 30px; }
</style>
</head>
<body>
<main class="flyer">
  <header class="hero">
    <div class="hero-photo" role="img" aria-label="State capitol building with a domed roof lit at dusk, trees in front, fading into a light left side"></div>
    <div class="state-mark">
      <div class="state-name">Kestrel</div>
      <div class="state-office">Office of Shared Services</div>
    </div>
    <div class="unit-badge"></div>
    <div class="unit-office">Office of Shared Services</div>
    <h1 class="unit-name">KSO Talent Growth</h1>
  </header>

  <nav class="services">
    <div class="service service--consulting">
      <svg viewBox="0 0 56 56" fill="none" stroke="#fff" stroke-width="2.2" stroke-linejoin="round">
        <rect x="8" y="10" width="40" height="28" rx="2"/>
        <path d="M3 44h50l-3 5H6z"/>
        <rect x="18" y="14" width="20" height="10" rx="2"/>
        <path d="M24 24l-2 4 6-4"/>
        <circle cx="20" cy="32" r="2.5"/><circle cx="36" cy="32" r="2.5"/>
      </svg>
      <span class="service-label">CONSULTING</span>
    </div>
    <div class="service service--workshops">
      <svg viewBox="0 0 56 56" fill="none" stroke="#fff" stroke-width="2.2" stroke-linejoin="round" stroke-linecap="round">
        <rect x="8" y="6" width="40" height="28" rx="2"/>
        <path d="M14 26l8-8 6 5 12-11"/>
        <path d="M28 34v8M18 52l10-10 10 10"/>
      </svg>
      <span class="service-label">WORKSHOPS</span>
    </div>
    <div class="service service--tools">
      <svg viewBox="0 0 56 56" fill="none" stroke="#fff" stroke-width="2.2">
        <circle cx="20" cy="34" r="7"/>
        <circle cx="20" cy="34" r="12" stroke-width="5" stroke-dasharray="4 3.2"/>
        <circle cx="39" cy="17" r="5"/>
        <circle cx="39" cy="17" r="9.5" stroke-width="4" stroke-dasharray="3.5 3"/>
      </svg>
      <span class="service-label">TOOLS/RESOURCES</span>
    </div>
  </nav>

  <div class="body-photo" role="img" aria-label="Soft, faded photo of colleagues meeting around a table"></div>

  <section class="column column--who">
    <h2>Who We Are</h2>
    <p>KSO Talent Growth is a unit of the Statewide Talent Services team. We offer State of Kestrel agencies and entities forward thinking consulting and learning solutions services – with a focus on management development.</p>
    <p>Whether as a trusted advisor or hands-on coach, our goal is to help our clients in whatever capacity can be most useful and help them be successful. We have over 30 years of experience in the public and private sector helping clients solve problems and implement modern solutions that deliver results. Our management development consultants are certified CHP, TDA, LCI, and PXI professionals.</p>
    <p>We are flexible in how we work, but uncompromising on delivering value. We meet our clients where they are “today” regarding their individual management development needs and opportunities.</p>
  </section>

  <section class="column column--what">
    <h2>What We Do</h2>
    <p>Adapting to a rapidly changing world and future workforce is a defining challenge for today’s State of Kestrel leaders and managers. We help our enterprise HR partners and managers get “future-ready” and prepare for the modern workplace by helping them:</p>
    <ul class="focus-list">
      <li>Build transformational leaders</li>
      <li>Create a coaching culture</li>
      <li>Drive employee engagement</li>
    </ul>
    <p>Along with our client consulting services, we provide learning and development solutions that are relevant, experiential, and collaborative. Unlike many “one-size-fits-all” programs, we partner with our clients to customize solutions for their unique needs and situations.</p>
    <p>We pride ourselves on being “experts without ego” consultants who are committed to our client’s success.</p>
  </section>

  <div class="quote"></div>
  <p class="quote-text">“Effective management is all about managing in the short term, while also preparing for the future…”</p>
  <p class="quote-credit">- Dana Whitfield, KSO Management Consultant</p>
</main>
</body>
</html>
```